PACKAGING DESIGN FOR ESSENTIAL OIL

The product is argan oil and I would be selling it in 30ml amber glass bottle.
I am looking for a design to put on the bottle. The brand name is BRUME DOUCE (Soft Mist translated in english). I would be using screen printing for the design on the glass bottle.
The bottle would be put in a carton box and I would need a design for that as well. I would like the carton box to be in gold colour (but you can propose a design with any other colour for the carton as well).
I am sending a picture with measurements of the glass bottle with its cap on it.
I am also sending the details I want to be included on the carton box.
I would like a design related to Morocco as the argan oil is from Morocco.
I have uploaded images that can inspire you all for my design.
I am sending you as well a link from findpix for Moroccan Mosaic:
https://www.findpix-example.test/search?q=argan+oil+brand&source=lnms&tbm=isch&sa=X&ei=aVZaUuKfFM7nrAeS7oGQAQ&ved=0CAcQ_AUoAQ&biw=1280&bih=658&dpr=1#q=moroccan+mosaic&tbm=isch&imgdii=_
Industry/Entity Type
Screen Printing
Requirements
Must have
- The Moroccan touch must be present in the design.
I would also like to have the brand name Brume Douce hot foil printed.
Nice to have
- A design of the argan tree would be nice as it shows exactly what we are selling.

```html
<!DOCTYPE html>
<html lang="fr">
<head>
<meta charset="utf-8">
<title>Brume Douce – Huile d'Argan, packaging</title>
<link href="https://fonts.googleapis.com/css2?family=Cinzel:wght@400;600&family=Arimo:wght@700&display=swap" rel="stylesheet">
<style>
  :root {
    --gold-dark: #7a5512;
    --gold-mid: #c08a2c;
    --gold-light: #f3d27a;
    --gold-text: #b88a3e;
    --gold-soft: #c9ad82;
    --maroon: #6e2438;
    --maroon-deep: #4f1526;
    --amber: #6b320c;
    --amber-light: #a55a1e;
    --paper: #ffffff;
    --stage: #e9e8ea;
    --panel-text: #f2e4bd;
  }
  * { margin: 0; padding: 0; box-sizing: border-box; }
  html, body { width: 1200px; height: 873px; overflow: hidden; background: var(--paper); }
  .board { position: relative; width: 1200px; height: 873px; font-family: "Cinzel", serif; }

  .box-front, .box-side {
    position: absolute; top: 0;
    background: linear-gradient(90deg, var(--gold-dark) 0%, var(--gold-light) 18%, var(--gold-mid) 35%, var(--gold-light) 55%, var(--gold-dark) 72%, var(--gold-light) 88%, var(--gold-mid) 100%);
  }
  .box-front { left: 0; width: 277px; height: 521px; }
  .box-band {
    position: absolute; left: 0; right: 0; top: 206px; height: 96px;
    background: var(--maroon);
    display: flex; align-items: center; justify-content: center; gap: 10px;
  }
  .seal {
    border-radius: 50%;
    background: radial-gradient(circle, var(--maroon) 0%, var(--maroon-deep) 100%);
    border: 3px solid var(--gold-mid);
    flex: none;
  }
  .box-band .seal { width: 70px; height: 70px; }
  .box-band .brand { color: var(--gold-light); font-size: 19px; font-weight: 600; letter-spacing: 1px; }

  .box-side { left: 305px; width: 220px; height: 511px; padding: 30px 14px 0 32px; }
  .box-side p, .box-side li {
    font-family: "Arimo", Arial, sans-serif; font-weight: 700;
    font-size: 8.4px; line-height: 10.2px; color: var(--panel-text);
  }
  .box-side p { margin-bottom: 10px; }
  .box-side ul { list-style: none; margin: -9px 0 18px 8px; }
  .box-side .spacer { height: 48px; }

  .bottle-stage { position: absolute; background: var(--stage); display: flex; justify-content: center; align-items: flex-end; }
  .stage-one { left: 570px; top: 0; width: 272px; height: 521px; }
  .stage-two { left: 870px; top: 391px; width: 330px; height: 482px; }
  .bottle-label {
    width: 190px; margin-bottom: 28px; padding: 24px 14px 16px;
    border-radius: 14px;
    background: linear-gradient(180deg, var(--amber-light) 0%, var(--amber) 60%, #3e1b06 100%);
    display: flex; flex-direction: column; align-items: center;
  }
  .stage-two .bottle-label { width: 220px; }
  .bottle-label .seal { width: 46px; height: 46px; margin-bottom: 12px; border-width: 2px; }
  .bottle-label .brand { color: var(--gold-text); font-size: 19px; font-weight: 600; }
  .bottle-label .kind { color: #e9dcc7; font-size: 15px; margin-top: 4px; }
  .bottle-label .claim { color: #e9dcc7; font-size: 20px; margin-top: 22px; font-weight: 600; }
  .bottle-label .purity { color: #e9dcc7; font-size: 13px; }
  .bottle-label .volume { color: #e9dcc7; font-size: 7px; align-self: flex-end; margin-top: 2px; }

  .seal-large { position: absolute; left: 912px; top: 27px; width: 228px; height: 228px; border-width: 9px; }

  .flat-label { position: absolute; top: 655px; width: 200px; display: flex; flex-direction: column; align-items: center; }
  .label-en { left: 92px; }
  .label-fr { left: 322px; }
  .flat-label .seal { width: 78px; height: 78px; margin-bottom: 14px; }
  .flat-label .brand { color: var(--gold-text); font-size: 22px; font-weight: 600; }
  .flat-label .kind { color: var(--gold-soft); font-size: 17px; }
  .flat-label .claim { color: var(--gold-soft); font-size: 22px; margin-top: 28px; font-weight: 600; }
  .flat-label .purity { color: var(--gold-soft); font-size: 14px; }
  .flat-label .volume { color: var(--gold-soft); font-size: 7px; align-self: flex-end; margin-top: 8px; margin-right: 30px; }

  .brand-mark { position: absolute; left: 585px; top: 690px; display: flex; align-items: center; gap: 12px; }
  .brand-mark .dot { width: 34px; height: 34px; border-radius: 50%; background: var(--gold-mid); }
  .brand-mark .brand { color: var(--gold-mid); font-size: 30px; font-weight: 600; }
</style>
</head>
<body>
<main class="board">

  <section class="box-front">
    <div class="box-band">
      <div class="seal" role="img" aria-label="Médaillon bordeaux à motif de mosaïque marocaine"></div>
      <span class="brand">Brume Douce</span>
    </div>
  </section>

  <section class="box-side">
    <p>L'huile d'argan est extraite de l'amande du fruit de l'arganier, un arbre ancien et unique au monde qui pousse au Maroc. Exceptionnellement riche en acides gras essentiels, oméga 6, vitamine E et polyphénols, elle regorge de propriétés hautement hydratantes, antioxydantes et régénératrices.</p>
    <p>Brume Douce, composée à 100% d'huile d'argan, est pure, naturelle, non désodorisée, non raffinée, sans mélange et sans additif. Elle laisse une peau lisse, souple et protégée.</p>
    <p>Utilisations et bienfaits:</p>
    <ul>
      <li>- Anti-ride: diminue les rides en activant les fonctions vitales des cellules</li>
      <li>- Fortifiant: nourrit les cheveux dévitalisés et fortifie les ongles</li>
      <li>- Cicatrisant: adoucit et aide la peau à cicatriser</li>
      <li>- Apaisant: utilisé en friction pour apaiser les douleurs articulaires</li>
    </ul>
    <p>Composition:<br>100% Argania Spinosa kernel oil biologique</p>
    <div class="spacer"></div>
    <p>Conservation<br>À l'abri de la lumière et de la chaleur<br>USAGE EXTERNE SEULEMENT<br>Produit du Maroc<br>Importé et distribué par:</p>
    <p>Sud Essences Ltée<br>12, Rue des Cèdres, Rose-Hill,<br>Ile Maurice<br>Tel: 400 1234<br>Email: contact@sudessences.test</p>
  </section>

  <section class="bottle-stage stage-one">
    <div class="bottle-label">
      <div class="seal" role="img" aria-label="Médaillon bordeaux à motif de mosaïque marocaine"></div>
      <span class="brand">Brume Douce</span>
      <span class="kind">Argan Oil</span>
      <span class="claim">Organic</span>
      <span class="purity">100% Natural</span>
      <span class="volume">30 ML</span>
    </div>
  </section>

  <div class="seal seal-large" role="img" aria-label="Grand médaillon bordeaux à motif de mosaïque marocaine cerclé d'or"></div>

  <section class="bottle-stage stage-two">
    <div class="bottle-label">
      <div class="seal" role="img" aria-label="Médaillon bordeaux à motif de mosaïque marocaine"></div>
      <span class="brand">Brume Douce</span>
      <span class="kind">Huile d'Argan</span>
      <span class="claim">Biologique</span>
      <span class="purity">100% Natural</span>
      <span class="volume">30 ML</span>
    </div>
  </section>

  <section class="flat-label label-en">
    <div class="seal" role="img" aria-label="Médaillon bordeaux à motif de mosaïque marocaine"></div>
    <span class="brand">Brume Douce</span>
    <span class="kind">Argan Oil</span>
    <span class="claim">Organic</span>
    <span class="purity">100% Natural</span>
    <span class="volume">30 ML</span>
  </section>

  <section class="flat-label label-fr">
    <div class="seal" role="img" aria-label="Médaillon bordeaux à motif de mosaïque marocaine"></div>
    <span class="brand">Brume Douce</span>
    <span class="kind">Huile d'Argan</span>
    <span class="claim">Biologique</span>
    <span class="purity">100% Natural</span>
    <span class="volume">30 ML</span>
  </section>

  <section class="brand-mark">
    <span class="dot"></span>
    <span class="brand">Brume Douce</span>
  </section>

</main>
</body>
</html>
```